Professional Oral Surgery Referral Pad, Business Card, and Stationary Design

Hello,

I want to work with a designer for my startup Oral Surgery Practice called: Dorrel Creek Oral Surgery & Implant Center

Ideally I would like to choose a good/professional design and work with a designer all the way to fulfill ALL of our stationary needs including referral pads, business cards, letterheads, envelopes, notepads, email signature, etc.

I would like to see designs first and hopefully would like to work with the designer for the lifetime of my practice and wanting to develop a long-term professional relationship.

In terms of the logo I have attached our practice logo files: I want to stay within the 3 colorways of the logo: Navy Blue/Silver grey/White. I would like for you to be creative and incorporate the "V" as best you can (for example greyed out watermark, etc)

I have also attached in my files the full contact info of our office in a word document: which includes address, email address, phone, fax, cell, etc.

I have also attached a few examples of double sided referral pad we can draw inspiration from. In terms of the referral pad I would ideally like to have my logo nicely placed/incorporated to make it look professional, address of the practice and contact info, my name and credentials.

Referral pad must have lines for patient, date of birth, phone number, referring doctor name, odontogram of all adult teeth and pediatric teeth, nice and big - so easy for dentist to refer. Also a jaw drawing of the intraoral cavity. Below that should have comments to surgeon.

In terms of procedures, I would like to have options of IV sedation, extractions, wisdom teeth, bone graft, pathology, tmj, trauma, expose/bond, orthognathic, other (list below)

In the back we can have a greyed out map of my practice address and Instructions for patients should include to bring insurance documentation, medication list, etc.

The final nitty gritty details of the referral pad can be worked on once I am happy with the design.

Target Market(s)

Patients who need oral surgical services and dentist referrals

Industry/Entity Type

Oral and Maxillofacial Surgery

• I would leave it up to the designers!

Colors
0054AA
0677BA
7BADD7
CADEEF
E8F1F8

Requirements
Must have
• Professional/sleek/modern and three color ways same as logo (navy blue, silver gray, and white)
Nice to have
• I would like to highlight my logo especially the implant ā€œvā€ either as watermark or part of the header or footnote. I will leave it to the expertise of the designer

```html
<!DOCTYPE html>
<html lang="en">
<head>
<meta charset="utf-8">
<title>Dorrel Creek Oral Surgery – Referral Form</title>
<link href="https://fonts.googleapis.com/css2?family=Source+Sans+3:wght@400;600;700&display=swap" rel="stylesheet">
<style>
  :root {
    --navy: #1f3d82;
    --navy-dark: #1b3a7a;
    --grey-band: #f0f0f1;
    --grey-text: #7a7a7a;
    --line: #2a4488;
    --paper: #ffffff;
    --bg: #ffffff;
    --jaw-fill: #c9d1e0;
    --chart-fill: #e6e1d8;
  }
  * { box-sizing: border-box; margin: 0; padding: 0; }
  html, body { width: 1200px; height: 1200px; overflow: hidden; background: var(--bg); }
  body { font-family: "Source Sans 3", "Myriad Pro", sans-serif; color: var(--navy); position: relative; }

  .sheet {
    position: absolute; left: 296px; top: 180px; width: 607px; height: 841px;
    background: var(--paper); box-shadow: 5px 5px 6px rgba(0,0,0,.45);
  }
  .abs { position: absolute; }

  .brand-name {
    left: 38px; top: 24px; width: 250px;
    font-size: 17px; font-weight: 600; line-height: 1.15; color: var(--navy);
  }

  .contact { top: 74px; font-size: 8.6px; font-weight: 700; line-height: 11.5px; color: var(--navy); }
  .contact.doctor { left: 228px; }
  .contact.phones { left: 389px; padding-left: 6px; border-left: 1px solid var(--navy); }
  .contact.address { left: 478px; padding-left: 6px; border-left: 1px solid var(--navy); }

  .title-rule { left: 34px; top: 133px; width: 540px; height: 3px; background: var(--navy); }
  .title-pill {
    left: 210px; top: 121px; width: 190px; height: 26px; border-radius: 13px;
    background: var(--navy); color: #fff; font-size: 21px; font-weight: 600;
    text-align: center; line-height: 26px; letter-spacing: .2px;
  }

  .field { display: flex; align-items: flex-end; font-size: 21px; color: var(--navy); }
  .field .rule { flex: 1; border-bottom: 1px solid var(--navy); margin-left: 3px; margin-bottom: 5px; }
  .f-patient { left: 35px; top: 165px; width: 538px; }
  .f-dob { left: 35px; top: 207px; width: 262px; }
  .f-phone { left: 302px; top: 207px; width: 271px; }
  .f-ref { left: 35px; top: 248px; width: 538px; }

  .jaw-diagram { left: 50px; top: 288px; width: 200px; height: 138px; }
  .tooth-chart { left: 316px; top: 312px; width: 244px; height: 86px; }

  .procedure-tab {
    left: 0; top: 420px; width: 112px; height: 19px; background: var(--navy);
    color: #fff; font-size: 13px; font-weight: 600; line-height: 19px; padding-left: 26px;
  }
  .procedure-band { left: 0; top: 439px; width: 607px; height: 102px; background: var(--grey-band); }
  .checklist { list-style: none; font-size: 11px; color: var(--grey-text); }
  .checklist li { display: flex; align-items: center; height: 17.6px; }
  .checklist .box { width: 10px; height: 10px; border: 1.3px solid #555; margin-right: 5px; }
  .checklist.left { left: 27px; top: 446px; }
  .checklist.right { left: 280px; top: 446px; }

  .comments-label { left: 30px; top: 549px; font-size: 24px; font-weight: 600; }
  .comments-box { left: 27px; top: 576px; width: 554px; height: 62px; border: 1px solid var(--navy); }

  .instructions-head { left: 0; top: 640px; width: 607px; text-align: center; font-size: 13px; font-weight: 600; }
  .steps { left: 28px; top: 672px; width: 553px; font-size: 14px; font-weight: 600; line-height: 17px; }
  .step-appt { display: flex; align-items: flex-end; }
  .step-appt .rule { border-bottom: 1px solid var(--navy); margin: 0 3px 4px; }
  .step-appt .rule.date { flex: 1; }
  .step-appt .rule.time { width: 76px; margin-right: 0; }

  .notice { left: 0; top: 733px; width: 607px; text-align: center; font-size: 14px; line-height: 16.7px; color: var(--grey-text); }
  .notice p { width: 380px; margin: 0 auto; }

  .footer-band {
    left: 0; top: 809px; width: 607px; height: 32px; background: var(--navy-dark);
    color: #fff; font-size: 21px; text-align: center; line-height: 28px;
  }
</style>
</head>
<body>
<main class="sheet">
  <div class="abs brand-name">Dorrel Creek Oral Surgery &amp; Implant Center</div>

  <div class="abs contact doctor">Dr. Leland Hart, DDS<br>DCO Oral Surgery &amp; Implant Center</div>
  <div class="abs contact phones">Work: 555 014 2231<br>Fax: 555 014 2290</div>
  <div class="abs contact address">88 Alder Row<br>Dorrel Creek, CA 90210</div>

  <div class="abs title-rule"></div>
  <div class="abs title-pill">REFERRAL FORUM</div>

  <div class="abs field f-patient">Patient:<span class="rule"></span></div>
  <div class="abs field f-dob">Date of Birth:<span class="rule"></span></div>
  <div class="abs field f-phone">Patient Phone:<span class="rule"></span></div>
  <div class="abs field f-ref">Referred By Dr.:<span class="rule"></span></div>

  <div class="abs jaw-diagram" role="img" aria-label="Jaw diagram: side views of the jaw and upper and lower arches with numbered teeth">
    <svg width="200" height="138" viewBox="0 0 200 138">
      <rect x="0" y="36" width="58" height="52" rx="10" fill="var(--jaw-fill)"/>
      <rect x="140" y="36" width="58" height="52" rx="10" fill="var(--jaw-fill)"/>
      <ellipse cx="100" cy="32" rx="28" ry="32" fill="var(--jaw-fill)"/>
      <ellipse cx="100" cy="106" rx="28" ry="32" fill="var(--jaw-fill)"/>
    </svg>
  </div>

  <div class="abs tooth-chart" role="img" aria-label="Tooth chart of upper and lower adult teeth labelled molar, premolar, canine and incisors">
    <svg width="244" height="86" viewBox="0 0 244 86">
      <rect x="0" y="6" width="236" height="74" fill="var(--chart-fill)"/>
      <rect x="0" y="42" width="236" height="2" fill="var(--navy)"/>
    </svg>
  </div>

  <div class="abs procedure-tab">PROCEDURE:</div>
  <div class="abs procedure-band"></div>
  <ul class="abs checklist left">
    <li><span class="box"></span>IV sedation</li>
    <li><span class="box"></span>extractions</li>
    <li><span class="box"></span>wisdom teeth</li>
    <li><span class="box"></span>bone graft</li>
    <li><span class="box"></span>pathalogy</li>
  </ul>
  <ul class="abs checklist right">
    <li><span class="box"></span>tmj</li>
    <li><span class="box"></span>trauma</li>
    <li><span class="box"></span>expose/bond</li>
    <li><span class="box"></span>orthognathic</li>
    <li><span class="box"></span>other (listed below)</li>
  </ul>

  <div class="abs comments-label">Comments to Surgeon:</div>
  <div class="abs comments-box"></div>

  <div class="abs instructions-head">INSTRUCTIONS TO PATEINTS:</div>
  <div class="abs steps">
    <div class="step-appt">1. Your appointment is on<span class="rule date"></span>at<span class="rule time"></span></div>
    <div>2. Please bring MEDICAL and DENTAL Insurance information with you</div>
    <div>3. Visit www.DORRELCREEKSURGERY.com to register prior to appt.</div>
  </div>

  <div class="abs notice">
    <p>Do not eat or drink anything (even water) 6 hrs prior to appointment if you are having surgery that day.</p>
    <p>An adult driver must accompany you and remain present if you are having surgery</p>
  </div>

  <div class="abs footer-band">Email: info@dorrelcreeksurgery.com</div>
</main>
</body>
</html>
```